10 Labels for Wild Bird Food

Label Design Request for New Products
We are excited to announce the launch of 10 new products and are seeking vibrant, fun, and colorful labels to match their energy. Each label should measure 6 x 4 inches (152.4mm x 101.6mm) and must feature our brand logo. Additionally, please include all the necessary information as detailed in the attached Word document.

Let's make our products stand out on the shelves with eye-catching designs!

Target Market(s)

Wild Bird Food Buyers

Requirements
Must have
• Logo

```html
<!DOCTYPE html>
<html lang="en">
<head>
<meta charset="utf-8">
<title>Feather Feast – Wild Bird Food Labels</title>
<link href="https://fonts.googleapis.com/css2?family=Arimo:wght@700&family=Open+Sans:wght@400;700&family=Roboto+Condensed:wght@400;500&display=swap" rel="stylesheet">
<style>
  :root {
    --backdrop: #cccccc;
    --paper: #ffffff;
    --ink: #231f20;
    --text: #3a3a3a;
    --brand: #1a8a7e;
    --sunflower: #f15a29;
    --peanut: #774c24;
    --mealworm: #544843;
    --calci: #9c8676;
    --shell: #5a3a1d;
  }
  * { margin: 0; padding: 0; box-sizing: border-box; }
  html, body { width: 1200px; height: 2398px; overflow: hidden; background: var(--backdrop); }
  .sheet {
    position: relative;
    width: 1289px; height: 2576px;
    transform: scale(0.93096);
    transform-origin: 0 0;
  }
  .label {
    position: absolute;
    width: 497px; height: 745px;
    background: var(--paper);
    color: var(--ink);
  }
  .label--a { left: 107px; top: 108px; }
  .label--b { left: 674px; top: 108px; }
  .label--c { left: 107px; top: 910px; }
  .label--d { left: 674px; top: 910px; }
  .label--e { left: 382px; top: 1725px; }

  .warnings {
    position: absolute; left: 27px; top: 31px;
    font: 500 15px/19px "Roboto Condensed", sans-serif;
  }
  .net-weight {
    position: absolute; right: 27px; top: 30px;
    font: 500 19px/24px "Roboto Condensed", sans-serif;
  }
  .brand {
    position: absolute; left: 0; right: 0; top: 132px;
    display: flex; justify-content: center; align-items: center; gap: 10px;
  }
  .brand-dot { width: 22px; height: 22px; border-radius: 50%; background: var(--brand); }
  .brand-name {
    font: 700 30px/1 "Open Sans", sans-serif;
    color: var(--brand);
    letter-spacing: 0.5px;
  }
  .product-band {
    position: absolute; left: 0; right: 0; top: 214px; height: 150px;
    display: flex; align-items: center; justify-content: center; text-align: center;
    color: var(--paper);
    font: 700 50px/50px "Arimo", sans-serif;
    letter-spacing: 3px;
  }
  .product-band--large { font-size: 56px; line-height: 54px; }
  .band-sunflower { background: var(--sunflower); }
  .band-peanut { background: var(--peanut); }
  .band-mealworm { background: var(--mealworm); }
  .band-calci { background: var(--calci); }
  .band-shell { background: var(--shell); }

  .rule {
    position: absolute; left: 27px; right: 27px; top: 426px;
    height: 3px; background: #333;
  }
  .description {
    position: absolute; left: 27px; right: 27px; top: 448px;
    font: 400 12px/15.5px "Open Sans", sans-serif;
    color: var(--text);
  }
  .description h2 {
    font: 700 12px/15px "Open Sans", sans-serif;
    color: var(--ink);
    margin-bottom: 6px;
  }
  .description h3 {
    font: 700 12px/15px "Open Sans", sans-serif;
    color: var(--ink);
    margin-top: 9px;
  }
  .description .usage { font-size: 13px; line-height: 16.5px; }

  .batch-box {
    position: absolute; left: 27px; top: 670px;
    width: 205px; height: 46px;
    border: 2px solid #333;
    padding: 3px 6px;
    font: 400 12px/19px "Roboto Condensed", sans-serif;
  }
  .batch-box span { display: inline-block; width: 62px; }
  .supplier {
    position: absolute; left: 274px; top: 662px;
    font: 400 12px/14.5px "Roboto Condensed", sans-serif;
    white-space: nowrap;
  }
</style>
</head>
<body>
<main class="sheet">

  <article class="label label--a">
    <p class="warnings">Not for human consumption<br>May Contain Nuts</p>
    <p class="net-weight">Net Wt: 2900g</p>
    <div class="brand"><span class="brand-dot"></span><span class="brand-name">feather feast</span></div>
    <h1 class="product-band band-sunflower">SUNFLOWER<br>HEARTS</h1>
    <div class="rule"></div>
    <section class="description">
      <h2>Enhance Your Garden with the Best Bird Feed!</h2>
      <p>Transform your garden into a bird haven with our Sunflower Hearts 5L Bag, the ultimate bird food for attracting a wide variety of beautiful feathered friends. Packed with essential nutrients and energy, these premium sunflower hearts are a must-have for any bird enthusiast.</p>
      <h3>Easy to Use:</h3>
      <p class="usage">Simply fill your bird feeders, sprinkle on bird tables, or scatter on the ground to attract a delightful array of garden birds. Watch as they flock to your garden, bringing life, color, and joy to your outdoor space.</p>
    </section>
    <div class="batch-box"><span>Expiry Date</span>:<br><span>Batch</span>:</div>
    <p class="supplier">Feather Feast<br>Marlow Supplies, Brookfield Mill Business<br>Park, Ashby, AB12 3CD<br>Contact: sales@marlowsupplies.co.uk</p>
  </article>

  <article class="label label--b">
    <p class="warnings">Not for human consumption<br>May Contain Nuts</p>
    <p class="net-weight">Net Wt: 3100g</p>
    <div class="brand"><span class="brand-dot"></span><span class="brand-name">feather feast</span></div>
    <h1 class="product-band product-band--large band-peanut">PEANUTS</h1>
    <div class="rule"></div>
    <section class="description">
      <h2>Delight Your Garden Birds with Nutritious Peanuts!</h2>
      <p>Attract a vibrant variety of feathered friends to your garden with our Peanuts 5L Bag, the perfect choice for bird enthusiasts who want to provide their avian visitors with a high-energy, nutritious treat. Packed with essential nutrients, our premium peanuts are a favorite among many bird species, ensuring your garden becomes a lively and colorful sanctuary.</p>
      <h3>Easy to Use:</h3>
      <p class="usage">Fill your bird feeders, place on bird tables, or scatter on the ground to create an inviting space for birds. Watch as they flock to your garden, adding beauty and song to your outdoor area.</p>
    </section>
    <div class="batch-box"><span>Expiry Date</span>:<br><span>Batch</span>:</div>
    <p class="supplier">Feather Feast<br>Marlow Supplies, Brookfield Mill Business<br>Park, Ashby, AB12 3CD<br>Contact: sales@marlowsupplies.co.uk</p>
  </article>

  <article class="label label--c">
    <p class="warnings">Not for human consumption<br>May Contain Nuts</p>
    <p class="net-weight">Net Wt: 800g</p>
    <div class="brand"><span class="brand-dot"></span><span class="brand-name">feather feast</span></div>
    <h1 class="product-band band-mealworm">DRIED<br>MEALWORMS</h1>
    <div class="rule"></div>
    <section class="description">
      <h2>Elevate Your Bird Feeding Experience with Nutritious Mealworms!</h2>
      <p>Create a thriving bird haven in your garden with our Dried Mealworms 5L Bag, the ultimate protein-rich treat for your feathered friends. Ideal for attracting a wide range of bird species, these premium dried mealworms are packed with essential nutrients, ensuring your garden birds stay healthy and energetic</p>
      <h3>Easy to Use:</h3>
      <p class="usage">Add to your bird feeders, sprinkle on bird tables, or mix with other bird food to create an irresistible feast for your garden birds. Watch as they flock to your garden, bringing vibrant colors and joyful chirping to your outdoor space</p>
    </section>
    <div class="batch-box"><span>Expiry Date</span>:<br><span>Batch</span>:</div>
    <p class="supplier">Feather Feast<br>Marlow Supplies, Brookfield Mill Business<br>Park, Ashby, AB12 3CD<br>Contact: sales@marlowsupplies.co.uk</p>
  </article>

  <article class="label label--d">
    <p class="warnings">Not for human consumption<br>May Contain Nuts</p>
    <p class="net-weight">Net Wt: 2900g</p>
    <div class="brand"><span class="brand-dot"></span><span class="brand-name">feather feast</span></div>
    <h1 class="product-band product-band--large band-calci">CALCI<br>WORMS</h1>
    <div class="rule"></div>
    <section class="description">
      <h2>Boost Your Garden Birds' Health with Nutritious Calci Worms!</h2>
      <p>Attract a vibrant array of feathered friends to your garden with our Calci Worms 5L Bag, the ultimate calcium-rich treat for your avian visitors. Perfect for bird enthusiasts, these premium calci worms are packed with essential nutrients, ensuring your garden birds stay healthy, strong, and energetic.</p>
      <h3>Easy to Use:</h3>
      <p class="usage">Add to your bird feeders, sprinkle on bird tables, or mix with other bird food to create an irresistible feast for your garden birds. Watch as they flock to your garden, bringing vibrant colors and joyful chirping to your outdoor space</p>
    </section>
    <div class="batch-box"><span>Expiry Date</span>:<br><span>Batch</span>:</div>
    <p class="supplier">Feather Feast<br>Marlow Supplies, Brookfield Mill Business<br>Park, Ashby, AB12 3CD<br>Contact: sales@marlowsupplies.co.uk</p>
  </article>

  <article class="label label--e">
    <p class="warnings">Not for human consumption<br>May Contain Nuts</p>
    <p class="net-weight">Net Wt: 1350g</p>
    <div class="brand"><span class="brand-dot"></span><span class="brand-name">feather feast</span></div>
    <h1 class="product-band band-shell">PEANUTS<br>IN SHELL</h1>
    <div class="rule"></div>
    <section class="description">
      <h2>Delight Your Garden Birds with Nutritious, Fun-to-Crack Peanuts!</h2>
      <p>Transform your garden into a lively bird sanctuary with our Peanuts in Shell 5L Bag, the perfect choice for bird enthusiasts who want to provide their avian visitors with a delicious and engaging treat. Packed with essential nutrients, our premium in-shell peanuts are a favorite among many bird species, ensuring your garden becomes a bustling hub of bird activity.</p>
      <h3>Easy to Use:</h3>
      <p class="usage">Fill your bird feeders, place on bird tables, or scatter on the ground to create an inviting space for birds. Watch as they flock to your garden, adding beauty and song to your outdoor area.</p>
    </section>
    <div class="batch-box"><span>Expiry Date</span>:<br><span>Batch</span>:</div>
    <p class="supplier">Feather Feast<br>Marlow Supplies, Brookfield Mill Business<br>Park, Ashby, AB12 3CD<br>Contact: sales@marlowsupplies.co.uk</p>
  </article>

</main>
</body>
</html>
```